finlo-welt.de
Zielgruppe
Alle die kein Geld haben :-)
Aufgabenstellung
Unter finlo-welt.de sollen Informationen rund um Kredite, Kreditkarten, Bonvia usw. entstehen. Diese werden dann unter Subdomains wir konto.finlo-welt.de oder kreditkarte.finlo-welt.de laufen. Die Domain finlo-welt.de soll die Hauptdomain werden wofür ein Logo und ein Layout benötigt wird. Auf den einzelnen Seiten sollen später Reporte verkauft werden und relativ viel mit Plunko Werbung gearbeitet werden. Hier ein paar Beipspiele www.zahlwerk-mohnel.biz, www.lumvesta88.de, www.tanne-blau-heft.de, www.nordlicht-mappe-brief.de
Die genannten Seiten sind keine Meisterleistung in Design und sollen nur in etwa Inhalte und die Einbindung von Plunko Adbox wieder geben. Menüpunkte sind immer gleich und werden sein mit den Untertiteln wie bei www.zahlwerk-mohnel.biz.

```html
<!DOCTYPE html>
<html lang="de">
<head>
<meta charset="utf-8">
<title>finlo-welt</title>
<link rel="stylesheet" href="https://fonts.googleapis.com/css2?family=Arimo:wght@400;700&display=swap">
<style>
  :root {
    --bg: #ffffff;
    --ink: #222222;
    --muted: #5a5a5a;
    --logo: #6b6b6b;
    --red: #c0191b;
    --blue: #1b78c3;
    --green: #2ea326;
    --line: #dcdcdc;
    --on-color: #ffffff;
  }
  * { box-sizing: border-box; margin: 0; padding: 0; }
  html, body { width: 1200px; height: 973px; overflow: hidden; background: var(--bg); }
  body { position: relative; font-family: "Arimo", Arial, sans-serif; color: var(--ink); }

  .logo { position: absolute; left: 95px; top: 44px; font-size: 50px; color: var(--logo); font-weight: 400; letter-spacing: 1px; }

  .main-nav { position: absolute; top: 59px; left: 615px; font-size: 16px; color: var(--muted); }
  .main-nav a { position: absolute; white-space: nowrap; color: inherit; text-decoration: none; }

  .dropdown { position: absolute; left: 703px; top: 80px; width: 268px; height: 90px; background: var(--red); z-index: 2; color: var(--on-color); font-size: 13px; line-height: 16px; padding: 34px 0 0 56px; }
  .dropdown::before { content: ""; position: absolute; left: 0; top: -4px; width: 70px; height: 6px; background: var(--red); }

  .topic { position: absolute; top: 179px; width: 347px; height: 392px; color: var(--on-color); }
  .topic--credit { left: 39px; background: var(--red); }
  .topic--account { left: 431px; background: var(--blue); }
  .topic--debtfree { left: 827px; background: var(--green); }
  .topic h2 { font-size: 20px; font-weight: 700; text-align: center; margin-top: 17px; white-space: nowrap; }
  .topic p { font-size: 13px; line-height: 17px; padding-left: 36px; margin-top: 60px; white-space: nowrap; }
  .topic .ad-note { position: absolute; top: 228px; left: 0; width: 100%; text-align: center; padding: 0; margin: 0; }

  .ad-label { position: absolute; top: 623px; font-size: 28px; font-weight: 700; color: #000; }

  .promo { position: absolute; left: 39px; top: 711px; width: 1135px; height: 240px; border: 1px solid var(--line); }
  .promo .divider { position: absolute; left: 473px; top: 36px; width: 1px; height: 166px; background: var(--line); }
  .promo-media { position: absolute; }
  .promo-media--cash { left: 25px; top: 24px; width: 139px; height: 178px; background: linear-gradient(160deg, #c7cdb7, #8f9a7e 60%, #e0c9b5); }
  .promo-media--coins { left: 508px; top: 36px; width: 155px; height: 181px; background: linear-gradient(180deg, #ffffff 20%, #d9b56a 60%, #9c7a36); }
  .promo-text { position: absolute; top: 44px; }
  .promo-text h3 { font-size: 27px; font-weight: 400; color: #333; margin-bottom: 19px; letter-spacing: .5px; }
  .promo-text p { font-size: 13.5px; line-height: 21px; color: #333; }
</style>
</head>
<body>
  <div class="logo">finlo-welt</div>

  <nav class="main-nav">
    <a href="#" style="left:0">Startseite</a>
    <a href="#" style="left:94px">Kredite</a>
    <a href="#" style="left:167px">Girokonten</a>
    <a href="#" style="left:270px">Schuldenfrei</a>
    <a href="#" style="left:390px">Bestellen</a>
    <a href="#" style="left:487px">Kontakt</a>
  </nav>

  <div class="dropdown">evtl. ein dropdown<br>mit plunko anzeigen</div>

  <section class="topic topic--credit">
    <h2>Bonviafreie Kredite</h2>
    <p>hier wäre ein text über bonviafreie kredite<br>evtl. auch eine kurze auflistung der anbieter<br>gut wäre auch eine kleine illustration zu<br>dem thema</p>
    <p class="ad-note">hier evtl. plunko anzeigen statt der auflistung</p>
  </section>
  <section class="topic topic--account">
    <h2>Bonviafreies Girokonto</h2>
    <p>hier wäre ein text über bonviafreie konten<br>evtl. auch eine kurze auflistung der anbieter<br>gut wäre auch eine kleine illustration zu<br>dem thema</p>
    <p class="ad-note">hier evtl. plunko anzeigen statt der auflistung</p>
  </section>
  <section class="topic topic--debtfree">
    <h2>Schuldenfrei</h2>
    <p>hier wäre ein text über schuldenfreiheit<br>evtl. auch eine kurze auflistung der anbieter<br>gut wäre auch eine kleine illustration zu<br>dem thema</p>
    <p class="ad-note">hier evtl. plunko anzeigen statt der auflistung</p>
  </section>

  <div class="ad-label" style="left:48px">Plunko Anzeigen</div>
  <div class="ad-label" style="left:470px">Plunko Anzeigen</div>
  <div class="ad-label" style="left:887px">Plunko Anzeigen</div>

  <section class="promo">
    <div class="promo-media promo-media--cash" role="img" aria-label="Foto: Hand hält einen Fächer Geldscheine"></div>
    <div class="promo-text" style="left:182px">
      <h3>Ihr Geld!</h3>
      <p>Wir helfen Ihnen auf den Weg<br>zur Ihrer Schuldenfreiheit.<br>finlo-welt hat schon hunderten<br>von Schuldenern geholfen,<br>endlich wieder volle Taschen zu haben</p>
    </div>
    <div class="divider"></div>
    <div class="promo-media promo-media--coins" role="img" aria-label="Foto: Münzstapel mit steigender roter Kurve"></div>
    <div class="promo-text" style="left:752px">
      <h3>Kein Einkommen mehr?</h3>
      <p>Wir helfen Ihnen auf den Weg<br>zur Ihrer Schuldenfreiheit.<br>finlo-welt hat schon hunderten<br>von Schuldenern geholfen,<br>endlich wieder volle Taschen zu haben</p>
    </div>
  </section>
</body>
</html>
```